Flyer-Design für Einzel- und Großhandel für Tuningteile
Zielgruppe
Die HLV GmbH ist im Einzel- und Großhandel für Tuningteile seit 9 Jahren tätig. Schwerpunktmäßig beschäftigen wir uns mit AERO Carbon Anbauteilen aus Carbon, Ansaugsystemen, Tuningboxen, Ladeluftkühlern, Bremsen und Kupplungen. Wir betrieben 7 Onlineshops die nach Themen oder Ländern gegliedert sind.
Gesucht wird ein Paketbeileger, der ausschließlich in unsere eigenen Pakete beigelegt wird. Zielgruppe sind also Bestandskunden - Alter, Einkommen ist stark gemischt. Unsere Zielgruppe ist zu 95+% männlich.
Aufgabenstellung
Der Paketbeileger soll 3 Zwecke erfüllen:
1. Ein persönliches Danke für deine Bestellung von der Geschäftsführung/dem Team von HLV.
2. Eine Bitte, uns auf Sicher Kaufen, Plauderbuch oder Findolo zu bewerten (Versionen mit 5% Incentive und ohne)
3. Ein Hinweis darauf, dass wir 5 unterschiedliche Onlineshops haben:
- www.hl-vortex.de : Hochwertige Carbon Autoteile und Norvalo Ansaugsysteme
- www.tq7-laden.de: TQ7 von Winkel Rennwerk. Die besten Tuningboxen aus den USA!
- www.pmlkuehl.de: Hochleistungs Ladeluftkühler zu günstigen Preisen.
- www.stark-kiste.de: Hochfeste Pellham Motorsport-Kupplungen.
- www.haltekeil.de: Die besten Bremsen zu besten Preisen.
- www.dröhnrohr.de: Die besten Sportauspuffanlagen. Gönn dir laut!
(Das Wording kann gerne anders sein!)
Ansprüche an das Design:
- Der Flyer muss sehr hochwertig wirken und wird später auf entsprechendem Material gedruckt.
- Der Look muss exklusiv und qualitativ hochwertig sein.
- Maße sind frei wählbar. Das Design steht hier im Vordergrund. Alles was gut und exklusiv aussieht geht.
- Optimal wäre es, wenn die 3 Geschäftsführer mit Bild und eventuell Zitat im Flyer zu sehen sind.
Die Ziele des Flyers sind:
1. Zum WOW-Effekt beim Auspacken beizutragen
2. Bewertungen zu generieren
3. Cross-Sales in den anderen Shops anzustoßen und den Kunden klarmachen, welche Bandbreite von Produkten bei uns erhältlich ist.

```html
<!DOCTYPE html>
<html lang="de">
<head>
<meta charset="utf-8">
<title>HLV Paketbeileger</title>
<link href="https://fonts.googleapis.com/css2?family=Raleway:wght@300;400;500;700&family=Italianno&display=swap" rel="stylesheet">
<style>
  :root {
    --page: #dcdcdc;
    --edge: #ffffff;
    --black: #000000;
    --carbon-dark: #141414;
    --carbon-light: #242424;
    --white: #ffffff;
    --muted: #9a9a9a;
    --photo-dark: #2a2a2a;
    --photo-light: #9a9a9a;
  }
  html, body {
    margin: 0;
    padding: 0;
    width: 676px;
    height: 1200px;
    overflow: hidden;
    background: var(--edge);
  }
  .canvas {
    position: relative;
    width: 676px;
    height: 1200px;
    overflow: hidden;
    font-family: "Raleway", sans-serif;
    color: var(--white);
  }
  .backdrop {
    position: absolute;
    left: 0; top: 0;
    width: 664px; height: 1200px;
    background: var(--page);
  }
  /* Front side */
  .front {
    position: absolute;
    left: 63px; top: 46px;
    width: 539px; height: 537px;
    background: var(--black);
  }
  .product-photo {
    position: absolute;
    top: 115px;
    width: 106px; height: 106px;
    background: linear-gradient(135deg, var(--photo-light), var(--photo-dark) 70%);
  }
  .product-photo.exhaust { left: 86px; }
  .product-photo.grille { left: 217px; }
  .product-photo.spoiler { left: 348px; }
  .brand {
    position: absolute;
    left: 0; right: 0;
    top: 499px;
    display: flex;
    justify-content: center;
    align-items: center;
    gap: 8px;
    font-weight: 700;
    font-size: 15px;
    letter-spacing: 2px;
  }
  .brand-dot {
    width: 12px; height: 12px;
    border-radius: 50%;
    background: var(--white);
  }
  /* Back side */
  .back {
    position: absolute;
    left: 64px; top: 608px;
    width: 538px; height: 537px;
    background: var(--black);
  }
  .carbon-field {
    position: absolute;
    left: 300px; top: 0;
    width: 238px; height: 537px;
    background: linear-gradient(160deg, var(--carbon-light), var(--carbon-dark));
  }
  .headline {
    position: absolute;
    right: 269px; top: 25px;
    margin: 0;
    text-align: right;
    font-weight: 700;
    font-size: 32px;
    line-height: 34px;
  }
  .subline {
    position: absolute;
    right: 269px; top: 59px;
    margin: 0;
    text-align: right;
    font-weight: 300;
    font-size: 22px;
    line-height: 24px;
  }
  .message {
    position: absolute;
    right: 267px; top: 111px;
    margin: 0;
    text-align: right;
    font-size: 13.3px;
    line-height: 16.9px;
    letter-spacing: 0.9px;
  }
  .signature {
    position: absolute;
    right: 267px; top: 352px;
    margin: 0;
    font-family: "Italianno", cursive;
    font-size: 22px;
    letter-spacing: 1px;
  }
  .shops-label {
    position: absolute;
    left: 14px; top: 478px;
    font-weight: 700;
    font-size: 10.5px;
    color: var(--muted);
  }
  .shop-list {
    position: absolute;
    margin: 0; padding: 0;
    list-style: none;
    font-size: 11px;
    line-height: 16px;
    color: var(--muted);
  }
  .shop-list.first { left: 14px; top: 494px; }
  .shop-list.second { left: 162px; top: 478px; }
  .team-member {
    position: absolute;
    left: 300px; width: 238px;
    text-align: center;
  }
  .team-member.one { top: 25px; }
  .team-member.two { top: 172px; }
  .team-member.three { top: 316px; }
  .portrait {
    width: 101px; height: 101px;
    margin: 0 auto;
    background: linear-gradient(180deg, #bdbdbd, #5a5a5a);
  }
  .member-name {
    margin-top: 9px;
    font-size: 11px;
    letter-spacing: 1px;
  }
  .member-name strong { font-weight: 700; }
  .review-call {
    position: absolute;
    left: 300px; width: 238px; top: 478px;
    text-align: center;
    font-size: 11.5px;
    letter-spacing: 0.6px;
    color: var(--muted);
  }
  .social {
    position: absolute;
    left: 360px; top: 501px;
  }
</style>
</head>
<body>
<div class="canvas">
  <div class="backdrop"></div>

  <section class="front">
    <div class="product-photo exhaust" role="img" aria-label="Carbon-Heckdiffusor mit Doppelendrohr"></div>
    <div class="product-photo grille" role="img" aria-label="Frontschürze mit Kühlergrill und Carbonlippe"></div>
    <div class="product-photo spoiler" role="img" aria-label="Carbon-Heckspoiler am Kofferraumdeckel"></div>
    <div class="brand"><span class="brand-dot"></span><span>HL VORTEX</span></div>
  </section>

  <section class="back">
    <div class="carbon-field" role="img" aria-label="Carbonfaser-Struktur als Hintergrund"></div>

    <h1 class="headline">DANKE</h1>
    <p class="subline">ipsum dolor sit</p>
    <p class="message">Lorem ipsum dolor sit<br>amet, consectetur<br>adipiscing elit, sed do<br>eiusmod tempor<br>incididunt ut labore et<br>dolore magna aliqua. Ut<br>enim ad minim veniam,<br>quis nostrud exercitation<br>ullamco laboris nisi ut<br>aliquip ex ea commodo<br>consequat. Duis aute<br>irure dolor in<br>reprehenderit in nulla.</p>
    <p class="signature">Ihre HLV Team</p>

    <div class="shops-label">ONLINESHOPS</div>
    <ul class="shop-list first">
      <li>www.hl-vortex.de</li>
      <li>www.haltekeil.de</li>
    </ul>
    <ul class="shop-list second">
      <li>www.pmlkuehl.de</li>
      <li>www.tq7-laden.de</li>
      <li>www.stark-kiste.de</li>
    </ul>

    <div class="team-member one">
      <div class="portrait" role="img" aria-label="Porträtfoto des Geschäftsführers Lorenz Adler"></div>
      <div class="member-name">LORENZ <strong>ADLER</strong></div>
    </div>
    <div class="team-member two">
      <div class="portrait" role="img" aria-label="Porträtfoto des Geschäftsführers Jonas Wendt"></div>
      <div class="member-name">JONAS <strong>WENDT</strong></div>
    </div>
    <div class="team-member three">
      <div class="portrait" role="img" aria-label="Porträtfoto des Geschäftsführers Felix Brandauer"></div>
      <div class="member-name">FELIX <strong>BRANDAUER</strong></div>
    </div>

    <div class="review-call">Bitte besuchen Sie &amp; bewerten uns!</div>
    <svg class="social" width="120" height="26" viewBox="0 0 120 26" aria-label="Plauderbuch, Bildfang, Filmkanal, Findolo">
      <g fill="none" stroke="#bdbdbd" stroke-width="1.2">
        <circle cx="12.5" cy="13" r="11"/>
        <circle cx="43.5" cy="13" r="11"/>
        <circle cx="74.5" cy="13" r="11"/>
        <circle cx="105.5" cy="13" r="11"/>
      </g>
    </svg>
  </section>
</div>
</body>
</html>
```